Photojournalism/photography business needs a simple, timeless & professional letterhead design

We need a letterhead design for photography/photojournalism business called 'qolvb', no capitals.

The letterhead needs to be:
- simple
- professional
- timeless
- easy to read
- consists of at least 2 colors to make it stands out.

We do mainly editorial photography, photo articles for various publications, travel, businesses, as well as people such as family and kids.

The final design should communicate professionalism, easy identification, attention grabbing, even if it has to be found among a stack of various papers on the clients' desks.

Target Market(s)

Various publications.

Industry/Entity Type

Business

Requirements
Must have
• Please use the logo attached.

```html
<!DOCTYPE html>
<html lang="en">
<head>
<meta charset="utf-8">
<title>qolvb letterhead</title>
<link href="https://fonts.googleapis.com/css2?family=Arimo:wght@400;700&display=swap" rel="stylesheet">
<style>
  :root {
    --backdrop: #d6d6d6;
    --paper: #ffffff;
    --ink: #1e1e1e;
    --ink-soft: #555555;
    --accent: #4a8fcb;
  }
  * { box-sizing: border-box; margin: 0; padding: 0; }
  html, body {
    width: 1200px; height: 847px; overflow: hidden;
    background: var(--backdrop);
    font-family: "Arimo", Arial, sans-serif;
    color: var(--ink);
  }
  .letterhead {
    position: absolute; left: 317px; top: 24px;
    width: 566px; height: 800px;
    background: var(--paper);
    padding: 34px 52px 0;
  }
  .brand {
    text-align: center;
    font-weight: 700; font-size: 34px; letter-spacing: -0.5px;
    color: var(--ink); line-height: 1;
  }
  .rule { height: 1px; background: var(--accent); }
  .rule--head { margin: 16px 0 24px; }
  .greeting { font-size: 9.5px; margin-bottom: 10px; }
  .body p {
    font-size: 9px; line-height: 1.55; text-align: justify;
    margin: 0 0 14px 14px;
  }
  .sign-off { text-align: right; margin-top: 18px; padding-right: 14px; }
  .signature {
    display: inline-block; width: 130px; height: 30px;
    background: linear-gradient(90deg, #f2f2f2, #e4e4e4);
  }
  .signer { font-size: 9px; line-height: 1.35; margin-top: 4px; }
  .rule--foot { margin: 18px 0 14px; }
  .contact {
    display: flex; font-size: 8.5px; line-height: 1.6; color: var(--ink-soft);
  }
  .contact__block { padding: 2px 18px; }
  .contact__block:first-child { padding-left: 38px; width: 215px; }
  .contact__block + .contact__block { border-left: 1px solid var(--accent); }
</style>
</head>
<body>
  <main class="letterhead">
    <header>
      <div class="brand">qolvb</div>
      <div class="rule rule--head"></div>
    </header>

    <section class="body">
      <p class="greeting">Dear Client,</p>
      <p>Lorem ipsum dolor sit amet, consectetur adipisicing elit, sed do eiusmod tempor incididunt ut labore et dolore magna aliqua. Ut enim ad minim veniam, quis nostrud exercitation ullamco laboris nisi ut aliquip ex ea commodo consequat. Duis aute irure dolor in reprehenderit in voluptate velit esse cillum dolore eu fugiat nulla pariatur. Excepteur sint occaecat cupidatat non proident, sunt in culpa qui officia deserunt mollit anim id est laborum.</p>
      <p>Lorem ipsum dolor sit amet, consectetur adipisicing elit, sed do eiusmod tempor incididunt ut labore et dolore magna aliqua. Ut enim ad minim veniam, quis nostrud exercitation ullamco laboris nisi ut aliquip ex ea commodo consequat. Duis aute irure dolor in reprehenderit in voluptate velit esse cillum dolore eu fugiat nulla pariatur. Excepteur sint occaecat cupidatat non proident, sunt in culpa qui officia deserunt mollit anim id est laborum.</p>
      <p>Lorem ipsum dolor sit amet, consectetur adipisicing elit, sed do eiusmod tempor incididunt ut labore et dolore magna aliqua. Ut enim ad minim veniam, quis nostrud exercitation ullamco laboris nisi ut aliquip ex ea commodo consequat. Duis aute irure dolor in reprehenderit in voluptate velit esse cillum dolore eu fugiat nulla pariatur. Excepteur sint occaecat cupidatat non proident, sunt in culpa qui officia deserunt mollit anim id est laborum.</p>
      <p>Lorem ipsum dolor sit amet, consectetur adipisicing elit, sed do eiusmod tempor incididunt ut labore et dolore magna aliqua. Ut enim ad minim veniam, quis nostrud exercitation ullamco laboris nisi ut aliquip ex ea commodo consequat. Duis aute irure dolor in reprehenderit in voluptate velit esse cillum dolore eu fugiat nulla pariatur. Excepteur sint occaecat cupidatat non proident, sunt in culpa qui officia deserunt mollit anim id est laborum.</p>
      <p>Lorem ipsum dolor sit amet, consectetur adipisicing elit, sed do eiusmod tempor incididunt ut labore et dolore magna aliqua. Ut enim ad minim veniam, quis nostrud exercitation ullamco laboris nisi ut aliquip ex ea.</p>
    </section>

    <section class="sign-off">
      <div class="signature" role="img" aria-label="Handwritten signature of Mara Ellison"></div>
      <div class="signer">Mara Ellison<br>Executive manager</div>
    </section>

    <footer>
      <div class="rule rule--foot"></div>
      <div class="contact">
        <div class="contact__block">1482 Harlow Creek Rd,<br>Brindlemoor Qld 4519</div>
        <div class="contact__block">mobile: 987 210 4433<br>phone: 1 (0) 765 2204</div>
        <div class="contact__block">web www.qolvb.com<br>www.socialpage.com/qolvb</div>
      </div>
    </footer>
  </main>
</body>
</html>
```